Laptop Accessories Packing Design

We are looking for a new package design of a laptop accesories (batteries, charges, hard drives etc.). We want to refresh our brand Vireo CellWorks. At VireoCell, we create high-end laptop accessories that ensure reliability, performance, and longevity for users worldwide. Our mission is to deliver innovative and durable solutions that allow users to work, create, and grow without limits.
General Packaging Concept
Minimalist and elegant look, yet with elements that catch the eye (Vireo products will mainly be offered on auction portals such as Brindle, Kiva, Tollmart, so it would be good if the packaging attracted attention and stood out from the competitors).
Should I put a photo, sketch or product icon on the box? We'll leave that to your imagination.
We ask for a general design of the packaging. After the competition, together with the winner, we will add the rest of the information to the back and sides of the box.
In the attachments there is our Logo (you can use other colors) and sample packaging of competitors
Target Market(s)
E-commerse
Industry/Entity Type
individual end customer
Look and feel
Each slider illustrates characteristics of the customer's brand and the style your logo design should communicate.

```html
<!DOCTYPE html>
<html lang="en">
<head>
<meta charset="utf-8">
<title>Vireo CellWorks – Box Front</title>
<link rel="stylesheet" href="https://fonts.googleapis.com/css2?family=Poppins:ital,wght@0,700;1,300&display=swap">
<style>
  :root {
    --page-bg: #ffffff;
    --box-black: #000000;
    --brand-yellow: #e8e03a;
    --glow-yellow: #d8d23a;
    --deep-olive: #3a3a08;
    --text-white: #ffffff;
  }
  html, body {
    margin: 0;
    padding: 0;
    width: 1200px;
    height: 1200px;
    overflow: hidden;
    background: var(--page-bg);
  }
  .canvas {
    position: relative;
    width: 1200px;
    height: 1200px;
  }
  .box-front {
    position: absolute;
    left: 80px;
    top: 342px;
    width: 1040px;
    height: 516px;
    background: var(--box-black);
    overflow: hidden;
  }
  .circuit-art {
    position: absolute;
    left: 36%;
    top: 0;
    right: 0;
    bottom: 0;
    background:
      radial-gradient(circle at 62% 48%, rgba(216,210,58,0.85) 0%, rgba(150,145,30,0.55) 18%, rgba(70,68,12,0.35) 38%, rgba(0,0,0,0) 62%),
      radial-gradient(ellipse at 12% 55%, rgba(90,88,10,0.45) 0%, rgba(0,0,0,0) 40%),
      var(--box-black);
  }
  .brand-name {
    position: absolute;
    left: 37px;
    top: 38px;
    margin: 0;
    font-family: "Poppins", sans-serif;
    font-weight: 700;
    font-size: 46px;
    line-height: 1;
    letter-spacing: -0.5px;
    color: var(--brand-yellow);
  }
  .tagline {
    position: absolute;
    left: 56px;
    top: 373px;
    margin: 0;
    font-family: "Poppins", sans-serif;
    font-style: italic;
    font-weight: 300;
    font-size: 23px;
    line-height: 35px;
    letter-spacing: 2.6px;
    color: var(--text-white);
    text-transform: uppercase;
  }
</style>
</head>
<body>
  <div class="canvas">
    <section class="box-front">
      <div class="circuit-art" role="img" aria-label="Glowing yellow circuit-board illustration with radiating traces and light sparks"></div>
      <h1 class="brand-name">Vireo CellWorks</h1>
      <p class="tagline">High End<br>Laptop Accesories</p>
    </section>
  </div>
</body>
</html>
```